Lumbra K - Premium Business Cards

Background of Lumbra K
Lumbra Kestrelwood is a cigar mobile lounge where guests become family. A place of luxury, relaxation, and ambiance is the global popularity demand. Lumbra Kestrelwood strives to provide first-class service of quality and products. Our goal is to ensure that every guest is treated and serviced as a VIP.

Lumbra Kestrelwood was founded by Desmond Harkavy Jr in January 2020. After 15 years of cigar reviews and research Desmond decided it was time to launch his own cigar brand and boutique cigar company. With a wealth of knowledge and years of experience Lumbra Kestrelwood was born. With opulence for all cultures, Lumbra Kestrelwood offers hand rolled cigars with premium blend tobacco from sweet to bold imported from Costa Rica, Dominican Republic, and Nicaragua. Thank you for your business!

Objective:
Create a business card template to be used for all employees. Design should communicate premium and classy. And should use earth tone colors.

Design should include:
1. Client wants to incorporate the cigar leaf
2. Logo
3. Tagline: Respect the smoke
3. Content info:
Calvin Mertzlow
Owner
555-617-0384
cmertzlow@lumbrawares.example
lumbrakestrelwood.example

```html
<!DOCTYPE html>
<html lang="en">
<head>
<meta charset="utf-8">
<title>Lumbra K — Business Cards</title>
<link href="https://fonts.googleapis.com/css2?family=Roboto+Condensed:wght@400;700&display=swap" rel="stylesheet">
<style>
  :root {
    --page: #ececec;
    --card: #ffffff;
    --ink: #231f20;
    --ink-soft: #3a3536;
    --leaf-dark: #3b2417;
    --leaf-mid: #6e4a33;
    --leaf-light: #9a7457;
    --on-dark: #ffffff;
  }
  * { box-sizing: border-box; margin: 0; padding: 0; }
  html, body {
    width: 1200px; height: 1200px; overflow: hidden;
    background: var(--page);
    font-family: "Roboto Condensed", "Arial Narrow", sans-serif;
    color: var(--ink);
  }
  .sheet { position: relative; width: 1200px; height: 1200px; }
  .card {
    position: absolute; left: 257px; width: 686px; height: 390px;
    border-radius: 20px; overflow: hidden;
    box-shadow: 0 10px 24px rgba(0,0,0,0.18);
  }
  .card--front { top: 165px; background: var(--card); }
  .card--back { top: 653px; }

  /* leaf-and-smoke artwork area across the top of the front */
  .leaf-art {
    position: absolute; left: 124px; top: 42px; width: 510px; height: 96px;
    border-radius: 48px;
    background: linear-gradient(100deg, rgba(35,31,32,0.04) 0%, rgba(110,74,51,0.28) 55%, rgba(59,36,23,0.55) 100%);
  }

  .brand-mark {
    position: absolute; right: 44px; bottom: 28px;
    display: flex; align-items: center; gap: 9px;
    font-weight: 700; font-size: 22px; letter-spacing: 1px;
    color: var(--ink); text-transform: uppercase;
  }
  .brand-mark__dot { width: 12px; height: 12px; border-radius: 50%; background: var(--ink); }

  .holder { position: absolute; left: 58px; top: 200px; }
  .holder__name { font-weight: 700; font-size: 26px; letter-spacing: 0.3px; text-transform: uppercase; line-height: 1; }
  .holder__role { font-size: 15px; color: var(--ink-soft); margin-top: 5px; }
  .holder__rule { display: block; margin: 12px 0 14px; }

  .contact { list-style: none; }
  .contact li { display: flex; align-items: center; gap: 10px; font-size: 17px; line-height: 22px; color: var(--ink-soft); }
  .contact svg { width: 13px; height: 13px; flex: none; fill: var(--ink); }
  .contact strong { font-weight: 700; color: var(--ink); }

  .leaf-photo {
    position: absolute; inset: 0;
    background:
      radial-gradient(ellipse at 50% 35%, var(--leaf-light) 0%, transparent 55%),
      linear-gradient(160deg, var(--leaf-mid) 0%, var(--leaf-dark) 100%);
  }
  .lockup { position: absolute; left: 0; right: 0; top: 128px; text-align: center; color: var(--on-dark); }
  .lockup__name {
    font-weight: 700; font-size: 84px; line-height: 1; letter-spacing: 3px; text-transform: uppercase;
  }
  .lockup__sub {
    display: flex; align-items: center; justify-content: center; gap: 16px;
    margin-top: 12px; font-weight: 700; font-size: 27px; letter-spacing: 1px; text-transform: uppercase;
  }
  .lockup__rule { width: 96px; height: 6px; flex: none; }
  .tagline {
    position: absolute; left: 0; right: 0; bottom: 40px; text-align: center;
    color: var(--on-dark); font-size: 16px; letter-spacing: 4px; text-transform: uppercase;
  }
</style>
</head>
<body>
<main class="sheet">
  <section class="card card--front" aria-label="Business card front">
    <div class="leaf-art" role="img" aria-label="Drawn cigar leaf with rising smoke"></div>

    <div class="holder">
      <h1 class="holder__name">Calvin Mertzlow</h1>
      <p class="holder__role">Owner</p>
      <svg class="holder__rule" width="94" height="6" viewBox="0 0 94 6" aria-hidden="true">
        <line x1="3" y1="3" x2="91" y2="3" stroke="#231f20" stroke-width="1"/>
        <circle cx="3" cy="3" r="2.5" fill="#231f20"/>
        <circle cx="91" cy="3" r="2.5" fill="#231f20"/>
      </svg>
      <ul class="contact">
        <li>
          <svg viewBox="0 0 24 24" aria-hidden="true"><path d="M6.6 10.8a15.1 15.1 0 0 0 6.6 6.6l2.2-2.2c.3-.3.7-.4 1-.2 1.1.4 2.3.6 3.6.6.6 0 1 .4 1 1V20c0 .6-.4 1-1 1A17 17 0 0 1 3 4c0-.6.4-1 1-1h3.5c.6 0 1 .4 1 1 0 1.3.2 2.5.6 3.6.1.3 0 .7-.2 1z"/></svg>
          555-617-0384
        </li>
        <li>
          <svg viewBox="0 0 24 24" aria-hidden="true"><path d="M2 5h20v14H2z"/><path d="M3 6l9 7 9-7" fill="none" stroke="#fff" stroke-width="1.6"/></svg>
          cmertzlow@lumbrawares.example
        </li>
        <li>
          <svg viewBox="0 0 24 24" aria-hidden="true"><circle cx="12" cy="12" r="10"/><path d="M7 9c2 0 3 1 3 3s2 2 2 4M14 5c0 2 2 3 4 3" fill="none" stroke="#fff" stroke-width="1.6"/></svg>
          <span><strong>lumbrakestrelwood</strong>.example</span>
        </li>
      </ul>
    </div>

    <div class="brand-mark"><span class="brand-mark__dot"></span>Lumbra K</div>
  </section>

  <section class="card card--back" aria-label="Business card back">
    <div class="leaf-photo" role="img" aria-label="Close-up photograph of dried brown cigar tobacco leaves"></div>
    <div class="lockup">
      <h2 class="lockup__name">Lumbra K</h2>
      <p class="lockup__sub">
        <svg class="lockup__rule" viewBox="0 0 96 6" aria-hidden="true"><line x1="3" y1="3" x2="93" y2="3" stroke="#fff" stroke-width="1"/><circle cx="3" cy="3" r="2.5" fill="#fff"/><circle cx="93" cy="3" r="2.5" fill="#fff"/></svg>
        Kestrelwood
        <svg class="lockup__rule" viewBox="0 0 96 6" aria-hidden="true"><line x1="3" y1="3" x2="93" y2="3" stroke="#fff" stroke-width="1"/><circle cx="3" cy="3" r="2.5" fill="#fff"/><circle cx="93" cy="3" r="2.5" fill="#fff"/></svg>
      </p>
    </div>
    <p class="tagline">Respect the smoke</p>
  </section>
</main>
</body>
</html>
```